Professional Services/Construction Management (Millwork) Biz Cards

We've decided on a logo and have our color palette set, now we want to design some very professional looking cards that make a strong first impression - they'll reflect our tagline (that we're going to put on the back: Innovative. Professional. Leaders.

The example business card shows generally the direction we've been thinking of going for the back side - **but we're open to other ideas**

Target Market(s)

The cards should target more high-end (wealthy) owners and general contracting companies. We want them to convey a strong first impression - in a professional and not garish way.

Industry/Entity Type

Construction Company

Contact Information for Business Card

There needs to be a place for our company contractor's license number and business address. We want to also have people's names, titles, phone number, email address. The back can be the logo, tagline and web address

Requirements
Must have
• follow our color palette
Nice to have
• Font & Styles should compliment the Harrow Joinery fonts, but not necessarily match exactly

```html
<!DOCTYPE html>
<html lang="en">
<head>
<meta charset="utf-8">
<title>Harrow Joinery — Business Cards</title>
<link href="https://fonts.googleapis.com/css2?family=Questrial&family=Open+Sans:wght@700&display=swap" rel="stylesheet">
<style>
  :root {
    --brown: #5f5044;
    --taupe: #a0847c;
    --green: #62a044;
    --white: #ffffff;
    --ink: #111111;
    --text-font: "Questrial", "Century Gothic", sans-serif;
  }
  * { margin: 0; padding: 0; box-sizing: border-box; }
  html, body { width: 1200px; height: 1200px; overflow: hidden; background: var(--white); }
  .sheet { position: relative; width: 1200px; height: 1200px; font-family: var(--text-font); }

  .side-label {
    position: absolute; top: 410px;
    font-family: "Open Sans", Arial, sans-serif; font-weight: 700;
    font-size: 12px; color: var(--ink); letter-spacing: -0.2px;
  }
  .side-label.front { left: 39px; }
  .side-label.back { left: 615px; }

  .card {
    position: absolute; top: 436px; width: 550px; height: 355px;
    border-radius: 15px; overflow: hidden;
  }

  /* Front */
  .card-front { left: 39px; background: var(--white); }
  .front-top-band {
    position: absolute; left: 0; top: 0; width: 100%; height: 46px; background: var(--brown);
  }
  .license {
    position: absolute; right: 45px; top: 16px;
    font-size: 11px; color: var(--white); letter-spacing: 0.3px;
  }
  .front-bottom-band {
    position: absolute; left: 0; bottom: 0; width: 100%; height: 141px; background: var(--taupe);
  }
  .brand-mark {
    position: absolute; left: 45px; top: 64px; width: 132px; height: 132px;
    border-radius: 50%; background: var(--brown);
    display: flex; align-items: center; justify-content: center; text-align: center;
  }
  .brand-mark .brand-name {
    font-size: 18px; line-height: 1.15; color: var(--white); letter-spacing: 0.5px;
  }
  .person { position: absolute; right: 45px; top: 101px; text-align: right; color: var(--brown); }
  .person-name { font-size: 26px; line-height: 1; letter-spacing: 0.2px; }
  .person-title { font-size: 11px; margin-top: 6px; letter-spacing: 0.4px; }

  .address {
    position: absolute; left: 45px; top: 255px;
    font-size: 15px; line-height: 21px; color: var(--white);
  }
  .contacts {
    position: absolute; right: 44px; top: 257px; list-style: none;
    font-size: 10px; color: var(--white);
  }
  .contacts li {
    display: flex; align-items: center; justify-content: flex-end;
    height: 21px; gap: 10px;
  }
  .contacts svg { width: 12px; height: 12px; display: block; }

  /* Back */
  .card-back { left: 615px; background: var(--green); }
  .back-cutout { position: absolute; left: 0; top: 0; }
  .back-mark {
    position: absolute; left: -1px; top: 62px; width: 230px; height: 230px;
    border-radius: 50%; background: var(--brown);
    display: flex; align-items: center; justify-content: center; text-align: center;
  }
  .back-mark .brand-name {
    font-size: 30px; line-height: 1.15; color: var(--white); letter-spacing: 0.8px;
  }
  .web-address {
    position: absolute; left: 395px; top: 150px; transform: translateX(-50%);
    text-align: center; color: var(--white); font-size: 14px;
    line-height: 19px; letter-spacing: 4px;
  }
</style>
</head>
<body>
<main class="sheet">
  <p class="side-label front">Business Card Front</p>
  <p class="side-label back">Business Card Back</p>

  <section class="card card-front" aria-label="Business card front">
    <div class="front-top-band"></div>
    <p class="license">License # 0101010110</p>

    <div class="brand-mark"><span class="brand-name">Harrow<br>Joinery</span></div>

    <div class="person">
      <p class="person-name">Your Name</p>
      <p class="person-title">DIRECTOR</p>
    </div>

    <div class="front-bottom-band"></div>
    <p class="address">Your address<br>will be<br>placed here</p>

    <ul class="contacts">
      <li><span>00 00000 00</span>
        <svg viewBox="0 0 12 12" aria-hidden="true"><rect width="12" height="12" rx="1.5" fill="#fff"/><path d="M3.6 2.5l1.3 1.6-.7.9c.5 1.1 1.4 2 2.6 2.6l.9-.7 1.6 1.3-.7 1.2C5.8 9.2 2.8 6.2 2.4 3.2z" fill="#a0847c"/></svg>
      </li>
      <li><span>00 00000 00</span>
        <svg viewBox="0 0 12 12" aria-hidden="true"><rect width="12" height="12" rx="1.5" fill="#fff"/><rect x="3.5" y="2.5" width="5" height="3" fill="#a0847c"/><rect x="2.5" y="5.5" width="7" height="3.5" fill="#a0847c"/></svg>
      </li>
      <li><span>info@harrowjoinery.com</span>
        <svg viewBox="0 0 12 12" aria-hidden="true"><rect width="12" height="12" rx="1.5" fill="#fff"/><rect x="2.5" y="3.5" width="7" height="5" fill="none" stroke="#a0847c"/><path d="M2.5 3.5l3.5 3 3.5-3" fill="none" stroke="#a0847c"/></svg>
      </li>
    </ul>
  </section>

  <section class="card card-back" aria-label="Business card back">
    <svg class="back-cutout" width="550" height="355" viewBox="0 0 550 355" aria-hidden="true">
      <path d="M0 45 H116 A133 133 0 0 1 116 311 H0 Z" fill="#ffffff"/>
    </svg>
    <div class="back-mark"><span class="brand-name">Harrow<br>Joinery</span></div>
    <p class="web-address">www<br>harrowjoinery<br>com</p>
  </section>
</main>
</body>
</html>
```